Veltiwell- Comprehensive quality healthcare delivered at your door.

I am looking for brochures to help promote my business. My business name is Veltiwel (see attachment and logo). This is a new health delivery system designed to provide high quality care to elderly in their communities or at home.

See attachements. The logo is already designed.

As far as services provided (see attachment)

Target Market(s)

Elderly patients

Industry/Entity Type

Business

Font styles to use
Serif

Colors

Designer to choose colors to be used in the design.

```html
<!DOCTYPE html>
<html lang="en">
<head>
<meta charset="utf-8">
<title>Veltiwel Brochure</title>
<link rel="stylesheet" href="https://fonts.googleapis.com/css2?family=Comfortaa:wght@400;700&family=Exo+2:ital,wght@0,800;1,800&display=swap">
<style>
  :root{
    --orange:#f39a12;
    --orange-deep:#e8890a;
    --charcoal:#333333;
    --ink:#2b2b2b;
    --paper:#ffffff;
    --paper-grey:#f1f1f1;
    --stage:#e6e6e6;
    --accent-green:#2f3a14;
    --white:#ffffff;
  }
  *{margin:0;padding:0;box-sizing:border-box}
  html,body{width:968px;height:1200px;overflow:hidden}
  body{background:var(--stage);font-family:"Comfortaa",sans-serif;color:var(--ink);position:relative}
  .spread{position:absolute;left:44px;width:880px;height:540px;background:var(--paper);box-shadow:0 6px 18px rgba(0,0,0,.12);overflow:hidden}
  .spread--outside{top:20px}
  .spread--inside{top:620px;background:var(--paper-grey)}
  .spread svg.shapes{position:absolute;inset:0;width:880px;height:540px}
  .fold{position:absolute;top:0;bottom:0;width:1px;background:rgba(0,0,0,.06)}
  .fold--a{left:293px}.fold--b{left:586px}

  .section-title{font-family:"Exo 2",sans-serif;font-style:italic;font-weight:800;font-size:22px;letter-spacing:.5px;position:absolute}
  .section-title::before{content:"//";margin-right:4px}
  .section-title--light{color:var(--white);border-bottom:1px solid rgba(255,255,255,.8);padding-bottom:2px}
  .section-title--orange{color:var(--orange);border-bottom:1px solid var(--orange);padding-bottom:2px}

  .service-list{position:absolute;list-style:none;font-size:12.5px;line-height:1.45}
  .service-list li{position:relative;padding-left:18px}
  .service-list li::before{content:"";position:absolute;left:0;top:4px;width:9px;height:9px;border:1.5px solid currentColor;border-radius:50%}
  .service-list li::after{content:"";position:absolute;left:3px;top:8px;width:5px;height:1.5px;background:currentColor}
  .service-list--light{color:var(--white)}
  .service-list--dark{color:var(--ink)}

  .contact{position:absolute;left:340px;top:348px;width:230px}
  .contact h2{font-family:"Exo 2",sans-serif;font-weight:800;font-size:26px;color:var(--ink)}
  .contact p{font-size:13px;margin-top:2px;display:flex;align-items:center;gap:6px}
  .contact svg{width:11px;height:11px}

  .web{position:absolute;color:var(--white);font-weight:700;font-size:14px}

  .brand{position:absolute;left:620px;top:354px;width:230px;text-align:center}
  .brand-mark{width:48px;height:48px;border-radius:50%;background:var(--orange);margin:0 auto 8px}
  .brand-name{font-family:"Comfortaa",sans-serif;font-weight:700;font-size:22px;line-height:1.1;color:var(--ink);letter-spacing:1px}

  .stay{position:absolute;left:600px;top:172px;width:265px;color:var(--white)}
  .stay h2{font-family:"Exo 2",sans-serif;font-style:italic;font-weight:800;font-size:22px;margin-bottom:6px}
  .stay p{font-size:9.5px;line-height:1.35}
</style>
</head>
<body>

<section class="spread spread--outside" aria-label="Brochure outside">
  <svg class="shapes" viewBox="0 0 880 540">
    <defs>
      <linearGradient id="teamTone" x1="0" y1="0" x2="1" y2="1">
        <stop offset="0" stop-color="#e9eef2"/><stop offset=".5" stop-color="#cdd8e2"/><stop offset="1" stop-color="#f4f4f4"/>
      </linearGradient>
      <linearGradient id="clinicTone" x1="0" y1="0" x2="1" y2="0">
        <stop offset="0" stop-color="#d9dde2"/><stop offset="1" stop-color="#eae3dc"/>
      </linearGradient>
    </defs>
    <polygon role="img" aria-label="Photo of a smiling medical team with stethoscopes" fill="url(#teamTone)" points="470,0 880,0 880,300 400,300"/>
    <polygon fill="var(--orange)" points="0,0 520,0 400,300 370,300 0,300"/>
    <polygon role="img" aria-label="Photo of a doctor with a young patient and her mother" fill="url(#clinicTone)" points="0,300 380,300 320,425 0,425"/>
    <polygon fill="var(--orange)" points="600,295 880,295 880,345 620,345"/>
    <polygon fill="var(--orange)" points="0,440 70,440 55,470 0,470"/>
    <polygon fill="var(--charcoal)" points="75,440 880,440 880,448 830,478 58,478"/>
    <polygon fill="var(--orange)" points="840,485 880,485 880,520 810,520"/>
  </svg>
  <div class="fold fold--a"></div><div class="fold fold--b"></div>

  <h2 class="section-title section-title--light" style="left:40px;top:34px;width:200px">SERVICES</h2>
  <ul class="service-list service-list--light" style="left:40px;top:76px;width:240px">
    <li>Home</li>
    <li>Assisted Living</li>
    <li>Skilled Nursing</li>
    <li>Independent Living</li>
    <li>Home and Community Based Services</li>
    <li>Respite Care</li>
    <li>Rehabilitation</li>
    <li>Renna Learning Center</li>
    <li>Renna Learning®</li>
  </ul>

  <div class="contact">
    <h2>Contact Us</h2>
    <p><svg viewBox="0 0 12 12"><path d="M2.5 1l2 2.2-1 1.3a7 7 0 0 0 4 4l1.3-1 2.2 2-1.2 1.5C5.5 11 1 6.5 1 2.2z" fill="var(--ink)"/></svg>555-014-2290</p>
    <p><svg viewBox="0 0 12 12"><circle cx="4" cy="8" r="2.5" fill="none" stroke="var(--ink)" stroke-width="1.4"/><circle cx="8" cy="4" r="2.5" fill="none" stroke="var(--ink)" stroke-width="1.4"/></svg>www.veltiwel.com</p>
  </div>

  <span class="web" style="left:650px;top:311px">www.veltiwel.com</span>

  <div class="brand">
    <div class="brand-mark"></div>
    <div class="brand-name">VELTIWEL</div>
  </div>
</section>

<section class="spread spread--inside" aria-label="Brochure inside">
  <svg class="shapes" viewBox="0 0 880 540">
    <defs>
      <linearGradient id="bedsideTone" x1="0" y1="0" x2="1" y2="1">
        <stop offset="0" stop-color="#eef0f2"/><stop offset=".5" stop-color="#c9d3de"/><stop offset="1" stop-color="#e4dcd6"/>
      </linearGradient>
      <linearGradient id="wardTone" x1="0" y1="0" x2="1" y2="0">
        <stop offset="0" stop-color="#e2c8bd"/><stop offset="1" stop-color="#f0f0f0"/>
      </linearGradient>
      <linearGradient id="portraitTone" x1="0" y1="0" x2="0" y2="1">
        <stop offset="0" stop-color="#f5f5f5"/><stop offset="1" stop-color="#dcdcdc"/>
      </linearGradient>
    </defs>
    <polygon role="img" aria-label="Photo of a doctor caring for an elderly patient in a hospital bed" fill="url(#bedsideTone)" points="40,0 620,0 620,230 560,335 40,150"/>
    <polygon role="img" aria-label="Photo of a hospital room" fill="url(#wardTone)" points="620,0 880,0 880,140 620,160"/>
    <polygon fill="var(--orange)" points="610,160 880,150 880,300 835,345 565,345"/>
    <polygon fill="var(--accent-green)" points="880,300 880,320 858,345 835,345"/>
    <polygon role="img" aria-label="Portrait of a smiling female doctor with arms crossed" fill="url(#portraitTone)" points="630,370 880,370 880,540 600,540"/>
    <polygon fill="var(--accent-green)" points="290,470 318,470 303,492"/>
    <polygon fill="var(--orange)" points="300,470 600,470 578,520 300,520"/>
  </svg>
  <div class="fold fold--a"></div><div class="fold fold--b"></div>

  <h2 class="section-title section-title--orange" style="left:40px;top:172px;width:200px">SERVICES</h2>
  <ul class="service-list service-list--dark" style="left:40px;top:214px;width:245px">
    <li>Comprehensive primary care services</li>
    <li>Coordination of speciality care</li>
    <li>Chronic disease management such as COPD, Asthma, Diabetes mellitus, Heart disease like congestive heart failure, Alzheimer's dementia, etc...</li>
    <li>Transitional Care</li>
    <li>Skilled nursing visits for wound care, catheter care, ostomy</li>
  </ul>
  <ul class="service-list service-list--dark" style="left:325px;top:352px;width:250px">
    <li>Social services assessment</li>
    <li>Home health assistance</li>
    <li>Physical therapy</li>
    <li>Mental health</li>
    <li>Dental health</li>
    <li>Transportation</li>
  </ul>

  <div class="stay">
    <h2>STAY HOME</h2>
    <p>Veltiwel offers home and Community Based Services for adults who wish to continue to live independently in the comfort of their communities.</p>
    <p style="margin-top:4px">We provide on site services and deliver high quality healthcare at your door. Our experienced physicians coordinate care with our certified nurse practitioners and provide chronic care management, physical therapy, rehabilitation and medications management.</p>
  </div>

  <span class="web" style="left:370px;top:487px">www.veltiwel.com</span>
</section>

</body>
</html>
```